Quirky Label Design for an Exciting UK-Based Organic Skincare Company!

We need label designs across our range of products, we are a high quality yet quirky organic skincare company called Gently Lumora, we use frosted glass packaging, and we are just wanting one design done for now, but the winning designer we would want to work with to design the rest of the labels for us. We also want them to design business cards and other literature at some point and maybe even a website page.

Our label design will go on a 63mm tall frosted glass jar which is 62mm in diameter. The actual label dimensions should be, 170 mm (W) x 50 mm (H). The idea is so that it wraps around the whole jar with the design at one side (at the front) and the ingredients on another (at the back).

LABEL 1
Organic Polynesian Whipped Body Butter
Vanilla Bean
120ml

Made with Organic Shea and Cocoa Butters and exotic Monoi de Tahiti

Ingredients (INCI): Organic Raw Shea Butter (Butyrospermum Parkii), Organic Raw Cocoa Butter (Theobroma Cacao), Monoi de Tahiti (Coconut (Cocos nucifera) oil (and) Tiare (Gardenia tahitensis) flower), Organic Sweet Almond Oil (Prunus Amygdalus Dulcis), Organic Madagascan Vanilla Extract (Vanillin)

Handmade by Gently Lumora Ltd
14 Quillfield Lane, Bournemouth BH2 9RT, UK
Batch:

OPTIONAL WRITING (if it fits in):
100% Natural and Organic
Intensely Moisturising

LABEL 2
Mango Smoothie
120ml

Ingredients (INCI): Organic Raw Shea Butter (Butyrospermum Parkii), Organic Raw Cocoa Butter (Theobroma Cacao), Monoi de Tahiti (Coconut (Cocos nucifera) oil (and) Tiare (Gardenia tahitensis) flower), Organic Sweet Almond Oil (Prunus Amygdalus Dulcis), Organic Mango Flavour (Aroma)

Batch:

100% Natural and Organic
Intensely Moisturising

I have attached a picture of the jar we use and the lid we use for these products, as well as our logo. I've also attached a 'Handmade in Dorset' stamp which we'd like to go on there if possible, along with a shelf life symbol.

I am thinking the background colour of the labels will be either white or even brown paper colour. Perhaps it would be interesting to see it in both. UPDATE: We have decided on white background now, not brown.

The final design should denote handmade, organic, high quality, pure, yet quirky and original / unique. I am thinking perhaps a seemingly hand-drawn black leaf outline? Could fit the bill, but as I say, up to you. Something that says handmade yet professional.

I'd like to have the original Photoshop files from the winning designer so we can use them as a template for the rest of our horizontal labels.

Target Market(s)

Everyone that appreciates a good quality skincare product focusing on natural & organic. Price is mid-range to high

Industry/Entity Type

It Company

Requirements
Must have
• Must make the product look high quality & organic yet quirky and accessible. Must have our logo and the shelf life symbol and the writing as above.
Nice to have
• Nice to have the 'handmade' stamp attached, but not absolutely necessary if it doesn't fit within your design.

```html
<!DOCTYPE html>
<html lang="en">
<head>
<meta charset="utf-8">
<title>Gently Lumora – Whipped Body Butter Label</title>
<link href="https://fonts.googleapis.com/css2?family=Cinzel:wght@400;500&family=Raleway:wght@400;500;600;700&family=Roboto+Condensed:wght@400&display=swap" rel="stylesheet">
<style>
  :root {
    --page: #f1ede6;
    --paper: #faf5dc;
    --paper-deep: #f3ebc4;
    --ink: #2a2a2a;
    --brand-pink: #e8a8a6;
    --brand-red: #9e2a22;
    --gold: #b48a3a;
    --gold-light: #e8c66a;
    --bronze: #8a6a3a;
    --brown: #7a3a14;
    --amber: #d88a2a;
    --white: #ffffff;
  }
  * { margin: 0; padding: 0; box-sizing: border-box; }
  html, body { width: 1200px; height: 663px; overflow: hidden; background: var(--page); }
  .canvas { position: relative; width: 1200px; height: 663px; }

  .label {
    position: absolute; left: 30px; top: 166px;
    width: 1140px; height: 330px;
    font-family: "Raleway", sans-serif; color: var(--ink);
    overflow: hidden;
  }
  .label__paper {
    position: absolute; inset: 0;
    background: radial-gradient(ellipse at 50% 40%, var(--paper) 0%, var(--paper-deep) 100%);
  }
  .label__bands { position: absolute; left: 0; bottom: 0; width: 1140px; height: 80px; }

  /* Back panel */
  .ingredients { position: absolute; left: 17px; top: 14px; width: 297px; }
  .ingredients__title { font-weight: 700; font-size: 15px; margin-bottom: 10px; }
  .ingredients__list { font-size: 15.3px; line-height: 21px; text-align: justify; }

  .claims { position: absolute; left: 19px; top: 235px; display: flex; align-items: center; gap: 12px; }
  .claims__badge { width: 66px; height: 66px; border-radius: 50%; border: 2px solid var(--bronze); background: var(--paper); }
  .claims__text { font-weight: 600; font-size: 15px; line-height: 20px; }

  /* Front panel */
  .front { position: absolute; left: 331px; top: 0; width: 480px; height: 330px; text-align: center; }
  .brand-seal {
    position: absolute; left: 174px; top: 4px; width: 132px; height: 132px;
    border-radius: 50%; background: rgba(255,255,255,0.85);
    display: flex; align-items: center; justify-content: center;
  }
  .brand-seal__name {
    font-family: "Raleway", sans-serif; font-weight: 700; font-size: 24px; line-height: 28px;
    color: var(--brand-pink); text-transform: uppercase;
  }
  .product-title { position: absolute; left: 0; top: 158px; width: 100%; font-family: "Cinzel", serif; color: var(--ink); }
  .product-title__line1 { font-size: 24px; letter-spacing: 0.5px; line-height: 32px; }
  .product-title__line2 { font-size: 31px; letter-spacing: 0.3px; line-height: 40px; }
  .variant { position: absolute; left: 54px; top: 237px; width: 382px; height: 28px; }
  .variant__rule { position: absolute; top: 13px; left: 0; right: 0; height: 2px; background: var(--gold); }
  .variant__plate {
    position: absolute; left: 48px; top: 0; width: 286px; height: 28px;
    background: linear-gradient(180deg, #a08050, #6e5230);
    color: var(--white); font-family: "Raleway", sans-serif; font-weight: 500;
    font-size: 20px; letter-spacing: 6px; line-height: 28px;
  }
  .net-weight {
    position: absolute; left: 194px; top: 273px; width: 92px; height: 76px;
    border-radius: 50%; background: var(--white);
    font-family: "Roboto Condensed", sans-serif; color: var(--ink);
    padding-top: 8px;
  }
  .net-weight__label { font-size: 12px; line-height: 14px; }
  .net-weight__value { font-size: 24px; line-height: 28px; }

  /* Side panel */
  .maker { position: absolute; left: 810px; top: 0; width: 330px; height: 330px; text-align: center; }
  .maker__stamp {
    position: absolute; left: 121px; top: 13px; width: 86px; height: 86px;
    border-radius: 50%; border: 2px solid var(--ink); background: var(--white);
  }
  .maker__made-with { position: absolute; top: 104px; width: 100%; font-size: 14px; font-weight: 500; line-height: 19px; }
  .maker__brand { position: absolute; top: 186px; width: 100%; font-weight: 700; font-size: 18px; color: var(--brand-red); text-transform: uppercase; }
  .maker__company { position: absolute; top: 236px; width: 100%; font-weight: 700; font-size: 16.5px; color: var(--brand-red); }
  .maker__address { position: absolute; top: 258px; width: 100%; font-size: 14.5px; line-height: 20px; }
</style>
</head>
<body>
<div class="canvas">
  <section class="label" aria-label="Wrap-around jar label">
    <div class="label__paper" role="img" aria-label="Cream paper background with faint hand-drawn leaf and flower pattern"></div>

    <svg class="label__bands" viewBox="0 0 1140 80" preserveAspectRatio="none" aria-hidden="true">
      <path d="M0 80 L0 62 Q160 58 330 44 L330 80 Z" fill="var(--gold-light)"/>
      <path d="M0 80 L0 70 Q170 66 330 54 L330 80 Z" fill="var(--amber)"/>
      <path d="M330 36 Q570 26 810 30 L810 80 L330 80 Z" fill="var(--brown)"/>
      <path d="M330 52 Q570 40 810 46 L810 80 L330 80 Z" fill="var(--gold-light)"/>
      <path d="M330 66 Q570 58 810 62 L810 80 L330 80 Z" fill="var(--amber)"/>
      <path d="M810 44 Q980 58 1140 60 L1140 80 L810 80 Z" fill="var(--gold-light)"/>
      <path d="M810 56 Q980 68 1140 70 L1140 80 L810 80 Z" fill="var(--amber)"/>
    </svg>

    <div class="ingredients">
      <h2 class="ingredients__title">Ingredients (INCI):</h2>
      <p class="ingredients__list">Organic Raw Shea Butter (Butyrospermum Parkii), Organic Raw Cocoa Butter (Theobroma Cacao), Monoi de Tahiti (Coconut (Cocos nucifera) oil (and) Tiare (Gardenia tahitensis) flower), Organic Sweet Almond Oil (Prunus Amygdalus Dulcis), Organic Madagascan Vanilla Extract (Vanillin)</p>
    </div>

    <div class="claims">
      <div class="claims__badge" aria-hidden="true"></div>
      <p class="claims__text">100% Natural and Organic<br>Intensely Moisturising</p>
    </div>

    <div class="front">
      <div class="brand-seal"><span class="brand-seal__name">Gently<br>Lumora</span></div>
      <h1 class="product-title">
        <span class="product-title__line1">Organic Polynesian</span><br>
        <span class="product-title__line2">Whipped Body Butter</span>
      </h1>
      <div class="variant">
        <div class="variant__rule"></div>
        <div class="variant__plate">VANILLA BEAN</div>
      </div>
      <div class="net-weight">
        <div class="net-weight__label">Net Wt.</div>
        <div class="net-weight__value">120ml</div>
      </div>
    </div>

    <div class="maker">
      <div class="maker__stamp" aria-hidden="true"></div>
      <p class="maker__made-with">Made with<br>Organic Shea and Cocoa Butters<br>and exotic Monoi de Tahiti</p>
      <p class="maker__brand">Gently Lumora</p>
      <p class="maker__company">Handmade by Gently Lumora Ltd</p>
      <p class="maker__address">14 Quillfield Lane, Bournemouth<br>BH2 9RT, UK<br>Batch:</p>
    </div>
  </section>
</div>
</body>
</html>
```